Neues Layout für ein Element auf der Homepage
Anselm hat unsere Wunschdesign sehr schön umgesetzt. Die Kommunikation mit ihm ist sehr entspannt und er zeigte sich auch bei mehreren Änderungswünschen kooperativ. Gerne wieder. :)
Zielgruppe
Die krugbote ist ein Getränkesofortlieferant. Der Grundgedanke hinter der krugbote ist es nach Bestellung die Getränke innerhalb von 120 Minuten kostenfrei bis an die Wohnungs-, Haustür oder ins Büro zu liefern. Dabei bestellen die Kunden Getränke auf der Webseite, um sie dann vor Ort geliefert zu bekommen.
Die Zielgruppe der krugbote ist daher breit gefächert. Sie umfasst alle Personen, die ihre Getränke in Mehrwegflaschen kaufen und online bestellen wollen. Die Zielgruppe umfasst u.a. Studenten, Berufstätige, Familien, Singlehaushalte, ältere Personen als auch Gewerbe, die Getränke ins Büro liefern lassen.
Aufgabenstellung
Für die neue Website der krugbote soll ein Element auf der Homepage umgestaltet werden. Dafür sollte die Anordnung von acht Text- sowie Bildelementen neugestaltet werden. Drei dieser Elemente sollte prominent dargestellt werden. Die Bild- und die Textelemente sind vorgegeben und befinden sich im Anhang.
Es sollte lediglich der Aufbau und die farbliche Gestaltung neu designt werden. Dabei ist es gewünscht, dass das neue Design zum Corporate Design passt (siehe Anhang).

```html
<!DOCTYPE html>
<html lang="de">
<head>
<meta charset="utf-8">
<title>krugbote – Startseitenelement</title>
<link href="https://fonts.googleapis.com/css2?family=Titillium+Web:wght@400;600;700&display=swap" rel="stylesheet">
<style>
:root{
  --lime:#c5cf2b;
  --pink:#e9559a;
  --blue:#1a5b8c;
  --olive:#7a8c1e;
  --grey:#8c8c8c;
  --line:#dcdcdc;
  --white:#ffffff;
}
*{box-sizing:border-box;margin:0;padding:0}
html,body{width:946px;height:1200px;overflow:hidden;background:var(--white);font-family:"Titillium Web",sans-serif}
.canvas{position:relative;width:946px;height:1200px}
.abs{position:absolute}
.category{position:absolute;top:85px;height:64px;border:2px solid #eee;border-top:none;background:var(--white);text-align:center;font-size:10px;color:var(--grey)}
.category svg{display:block;margin:6px auto 4px}
.intro-title{left:0;width:1026px;top:220px;text-align:center;font-size:11px;font-weight:700;color:var(--blue)}
.usp-card{position:absolute;top:254px;width:119px;height:148px;border:2px solid var(--line);background:var(--white);text-align:center}
.usp-card svg{display:block;margin:12px auto 0}
.usp-band{position:absolute;top:70px;left:-4px;right:-4px;height:15px;background:var(--pink);color:var(--white);font-size:7px;font-weight:700;line-height:15px}
.usp-text{position:absolute;top:90px;left:8px;right:8px;font-size:6.5px;line-height:9px;color:#666}
.benefit-bar{left:101px;top:430px;width:781px;height:78px;background:var(--lime)}
.benefit{position:absolute;top:14px;width:90px;margin-left:-45px;text-align:center;color:var(--white);font-size:5.5px;font-weight:700}
.benefit svg{display:block;margin:0 auto 6px}
.brands{left:101px;top:508px;width:781px;height:143px;text-align:center}
.brands-rule{position:absolute;left:378px;top:10px;width:24px;height:2px;background:#e3e6b8}
.brands-title{position:absolute;left:0;right:0;top:20px;font-size:11px;font-weight:600;color:#555}
.brands-sub{position:absolute;left:0;right:0;top:35px;font-size:6px;color:#bbb}
.brand{position:absolute;top:90px;width:80px;margin-left:-40px;font-size:15px;font-weight:700}
.arrow-btn{position:absolute;top:92px;width:20px;height:20px;border-radius:50%;box-shadow:0 0 4px #ddd;font-size:10px;line-height:20px;color:#aaa}
.feature-panel{left:189px;top:754px;width:591px;height:154px;background:var(--lime)}
.feature-label{position:absolute;top:104px;width:140px;margin-left:-70px;text-align:center;font-size:13px;color:var(--white);white-space:nowrap}
.tooltip{left:450px;top:771px;width:288px;height:109px;background:var(--white);border:3px solid #ddd;box-shadow:4px 4px 0 #aaa;text-align:center;font-size:14.5px;line-height:18.5px;color:var(--grey);padding-top:6px}
</style>
</head>
<body>
<div class="canvas">

  <div class="category" style="left:263px;width:74px">
    <svg width="22" height="30" viewBox="0 0 22 30"><rect x="5" y="6" width="12" height="22" rx="2" fill="none" stroke="#e0b35a" stroke-width="2"/><rect x="7" y="14" width="8" height="12" fill="#f1d590"/></svg>Schorle</div>
  <div class="category" style="left:351px;width:74px">
    <svg width="24" height="30" viewBox="0 0 24 30"><path d="M5 8h14l-2 20H7z" fill="#8fdcc0" stroke="#2fb08a" stroke-width="2"/><circle cx="12" cy="5" r="4" fill="#2fb08a"/></svg>Saft</div>
  <div class="category" style="left:439px;width:74px">
    <svg width="22" height="30" viewBox="0 0 22 30"><path d="M5 3h12c0 9-3 13-6 13S5 12 5 3z" fill="none" stroke="#d23a5c" stroke-width="2"/><path d="M11 16v10M6 27h10" stroke="#d23a5c" stroke-width="2"/></svg>Wein</div>
  <div class="category" style="left:527px;width:74px">
    <svg width="22" height="30" viewBox="0 0 22 30"><ellipse cx="11" cy="15" rx="7" ry="11" fill="none" stroke="#c89a4a" stroke-width="2"/><path d="M11 5c-4 6 4 14 0 20" fill="none" stroke="#c89a4a" stroke-width="1.5"/></svg>Kaffee</div>
  <div class="category" style="left:615px;width:104px"></div>

  <div class="abs intro-title">Das ist die krugbote</div>

  <div class="usp-card" style="left:309px">
    <svg width="38" height="44" viewBox="0 0 38 44"><circle cx="19" cy="26" r="15" fill="none" stroke="var(--olive)" stroke-width="3"/><rect x="15" y="3" width="8" height="5" fill="none" stroke="var(--olive)" stroke-width="3"/><path d="M19 26l6-7" stroke="var(--olive)" stroke-width="3"/></svg>
    <div class="usp-band">LIEFERUNGEN IN 120 MINUTEN</div>
    <div class="usp-text">Ab Ihrer Bestellung.<br>Immer und ohne Aufpreis!<br>Montag bis Samstag<br>9 bis 21 Uhr</div>
  </div>
  <div class="usp-card" style="left:449px">
    <svg width="74" height="40" viewBox="0 0 74 40"><path d="M26 8h28l10 10h6v12H26z" fill="none" stroke="var(--olive)" stroke-width="3"/><circle cx="36" cy="31" r="5" fill="#fff" stroke="var(--olive)" stroke-width="3"/><circle cx="60" cy="31" r="5" fill="#fff" stroke="var(--olive)" stroke-width="3"/><path d="M2 12h18M6 18h16M2 24h20" stroke="var(--olive)" stroke-width="3"/></svg>
    <div class="usp-band">KEINE LIEFERGEBÜHR</div>
    <div class="usp-text">Alle Bestellungen erhalten<br>Sie kostenfrei bis an<br>Ihre Wohnungs- od.<br>Haustüre geliefert. Egal<br>in welchem Stockwerk<br>sich diese befindet.</div>
  </div>
  <div class="usp-card" style="left:589px">
    <svg width="44" height="44" viewBox="0 0 44 44">
      <path d="M8 20V11l2.5-3V3h3v5l2.5 3v9M28 20V11l2.5-3V3h3v5l2.5 3v9" fill="none" stroke="var(--olive)" stroke-width="2.5" stroke-linejoin="round"/>
      <rect x="3" y="20" width="38" height="22" fill="none" stroke="var(--olive)" stroke-width="3"/>
      <path d="M22 20v6" stroke="var(--olive)" stroke-width="3"/>
      <rect x="11" y="28" width="22" height="8" fill="none" stroke="var(--olive)" stroke-width="3"/>
    </svg>
    <div class="usp-band">BEQUEME PFANDRÜCKGABE</div>
    <div class="usp-text">Ihr Leergut nehmen wir<br>ganz einfach wieder mit.<br>Der Pfandbetrag wird<br>dann direkt von der<br>Rechnung abgezogen.</div>
  </div>

  <div class="abs benefit-bar">
    <div class="benefit" style="left:231px"><svg width="28" height="28" viewBox="0 0 28 28"><path d="M4 14L14 4h10v10L14 24z" fill="none" stroke="#fff" stroke-width="2"/><circle cx="19" cy="9" r="2" fill="#fff"/></svg>GÜNSTIGE PREISE</div>
    <div class="benefit" style="left:322px"><svg width="28" height="28" viewBox="0 0 28 28"><rect x="3" y="8" width="22" height="15" rx="2" fill="none" stroke="#fff" stroke-width="2"/><rect x="16" y="13" width="9" height="6" fill="none" stroke="#fff" stroke-width="2"/></svg>SICHER BEZAHLEN</div>
    <div class="benefit" style="left:420px"><svg width="28" height="28" viewBox="0 0 28 28"><path d="M2 5h4l3 13h14l3-10H8" fill="none" stroke="#fff" stroke-width="2"/><circle cx="11" cy="23" r="2" fill="#fff"/><circle cx="21" cy="23" r="2" fill="#fff"/></svg>GERINGER MINDESTBESTWERT</div>
    <div class="benefit" style="left:515px"><svg width="28" height="28" viewBox="0 0 28 28"><path d="M14 24L4 14a5.5 5.5 0 0 1 10-7 5.5 5.5 0 0 1 10 7z" fill="none" stroke="#fff" stroke-width="2"/></svg>PRIVAT UND GEWERBE</div>
    <div class="benefit" style="left:594px"><svg width="28" height="28" viewBox="0 0 28 28"><path d="M3 13h5v12H3zM8 13l5-9c3 0 3 3 2 6h8c2 0 3 2 2 4l-3 9c-1 2-2 2-3 2H8" fill="none" stroke="#fff" stroke-width="2"/></svg>NACHBARNETZ</div>
  </div>

  <div class="abs brands">
    <div class="brands-rule"></div>
    <div class="brands-title">Alle unsere Marken</div>
    <div class="brands-sub">alle anzeigen</div>
    <div class="arrow-btn" style="left:14px">‹</div>
    <div class="arrow-btn" style="right:-2px">›</div>
    <div class="brand" style="left:277px;color:#b08a3a">Talbrunn</div>
    <div class="brand" style="left:370px;color:#2a6db0">Teeblatt</div>
    <div class="brand" style="left:468px;color:#1d2f6b">Quellring</div>
    <div class="brand" style="left:563px;color:#d0303a">Perlhaus</div>
  </div>

  <div class="abs feature-panel">
    <svg class="abs" style="left:50px;top:40px" width="50" height="44" viewBox="0 0 50 44"><path d="M25 40L6 21A10.5 10.5 0 0 1 25 8a10.5 10.5 0 0 1 19 13z" fill="none" stroke="#fff" stroke-width="3.5"/></svg>
    <div class="feature-label" style="left:74px">PRIVAT UND GEWERBE</div>
    <svg class="abs" style="left:184px;top:36px" width="66" height="68" viewBox="0 0 66 68"><path d="M3 23h10v24H3zM13 23l10-18c6 0 6 6 4 11h16c4 0 6 4 4 8l-6 18c-2 4-4 5-6 5H13" fill="#fff" stroke="var(--blue)" stroke-width="3.5"/><path d="M24 30v34l8-9 7 13 6-3-7-13h12z" fill="#333" stroke="#fff" stroke-width="1"/></svg>
    <div class="feature-label" style="left:212px;color:var(--blue)">NACHBARNETZ</div>
  </div>

  <div class="abs tooltip">Folgen Sie uns auf Nachbarnetz<br>und verpassen Sie keine Aktion!<br>Unter allen Followern verlosen<br>wir jeden Monat einen<br>100 Euro Einkaufsgutschein.</div>

</div>
</body>
</html>
```